Book Cover for: TITLE Mend the Quiet Hours SUBTITLE For couples who don't want to break up

We need a full cover design for a book on relationships written by husband and wife team, Marla and Walter Dunmore, PhD. This book will offer hope for couples that are on the verge of breaking up but want to work things out and stay together. The theme is to teach couples about their own reactions to their partner, how moods affect a relationship, how to get creative to solving problems and how to have a good feeling towards your partner regardless of differences. This book is about hope. It is a positive look at relationships that feel hopeless.

Target Market(s)

Married or couples that are going through a difficult time and are considering splitting up due to, communication difficulties, addiction, affair. We imagine the book will appeal to women more than men but still want a cover that men would be comfortable picking up.

Colors

Designer to choose colors to be used in the design.

Requirements
Must have
• We want the cover to beautiful, intriguing, simple and uncomplicated. We don't want it overly busy, technical, or complex.
Nice to have
• MAYBE?? a broken heart being put back together.
Should not have
• No photo, no cartoon, no flowers, no couple (unless obscure and not gender specific).

```html
<!DOCTYPE html>
<html lang="en">
<head>
<meta charset="utf-8">
<title>Mend the Quiet Hours — Book Cover</title>
<link href="https://fonts.googleapis.com/css2?family=Old+Standard+TT:wght@400&display=swap" rel="stylesheet">
<style>
  :root {
    --page: #ffffff;
    --slate: #455659;
    --cream: #fde0bd;
    --thread: #c9a084;
    --heart: #ef4137;
    --heart-deep: #c8342e;
  }
  * { margin: 0; padding: 0; box-sizing: border-box; }
  html, body {
    width: 1200px;
    height: 1200px;
    overflow: hidden;
    background: var(--page);
  }
  .cover {
    position: absolute;
    left: 256px;
    top: 66px;
    width: 688px;
    height: 1070px;
    background: var(--slate);
    font-family: "Old Standard TT", Georgia, serif;
    color: var(--cream);
  }
  .title {
    position: absolute;
    inset: 0;
    font-weight: 400;
  }
  .title-line {
    position: absolute;
    font-size: 86px;
    line-height: 1;
    letter-spacing: -1px;
    white-space: nowrap;
  }
  .title-line.first  { left: 128px; top: 116px; }
  .title-line.second { left: 72px;  top: 196px; }
  .title-line.third  { left: 112px; top: 276px; }
  .subtitle {
    position: absolute;
    left: 420px;
    top: 290px;
    font-size: 25px;
    line-height: 26px;
    font-weight: 400;
    white-space: nowrap;
  }
  .artwork {
    position: absolute;
    left: 240px;
    top: 388px;
    width: 205px;
    height: 505px;
    border-radius: 100px;
    background: linear-gradient(180deg, var(--thread) 0%, var(--heart) 45%, var(--heart-deep) 70%, var(--thread) 100%);
    opacity: 0.85;
  }
  .authors {
    position: absolute;
    left: 169px;
    top: 930px;
    display: flex;
    align-items: flex-end;
    gap: 10px;
  }
  .authors-mark {
    width: 40px;
    height: 34px;
    background: var(--thread);
    opacity: 0.5;
  }
  .authors-name {
    font-size: 20px;
    line-height: 1;
    white-space: nowrap;
  }
</style>
</head>
<body>
  <main class="cover">
    <h1 class="title">
      <span class="title-line first">Mend</span>
      <span class="title-line second">the Quiet</span>
      <span class="title-line third">Hours</span>
    </h1>
    <p class="subtitle">For couples<br>who don't want<br>to break up</p>
    <div class="artwork" role="img" aria-label="Illustration of a red broken heart stitched together with a winding thread that ends in two overlapping speech bubbles"></div>
    <div class="authors">
      <div class="authors-mark" role="img" aria-label="Small line drawing of two figures holding hands"></div>
      <span class="authors-name">Marla e Walter Dunmore, PhD</span>
    </div>
  </main>
</body>
</html>
```